Brantley Estates is a commercial real estate development company based in the United States. We develop high-end office buildings and student housing apartments. We have a new logo and need to update all of our stationary items and business cards. We would like the design to be clean and professional. Our logo and color information is attached. Our logo MUST be in full color and not as white. It is preferred that the logo is on a white background.

Color code Blue R 0. G 62. B 124 ( #003E7C )
C 100 M84 Y 26 K 22
Black R32. G30. B30 ( #201E1E)
C100 M100 Y100 K100

Font used TRAJAN PRO3 PRO BOLD.

Items needed:
1. Business card - Leaning towards doing just a one side business card in a thicker paper. Include - logo, name - Martin E. Caldwell, Title - Chairman & CEO, 5120 Ridgemont Pkwy. Suite 400, Atlanta, GA 30327 - Cell number 404.617.####, Office 770.245.62## email@brantleyestates.com; www.brantleyestates.com.

2. Letterhead - Standard 8.5 by 11 paper. We do have a smaller size for the CEO that is 7.25 by 10.5 that is just a mirror of the letterhead except with his name (Martin E. Caldwell) and title (Chariman & CEO) listed at the top in the header. Letthead needs address, phone number and website, plus logo. *Prepared such that we can either implement as a Google Document template or professionally print.

3. Legal sized envelope - #10 envelope - which measures 4 1/8" by 9 1/2". We also use the same size envelope with a window. Need logo and address. A photo of the old envelope style is attached.

4. 9" x 12" Pocket folder - Need a design that can also be split to be a cover page and back - We use the cover pages in spiral binding machine, so we need to leave room on the left for that. One of the pockets should hold a business card. Include logo, address, phone, website. Also if text is needed, we could say development / leasing / property management.

5. Shipping label - 3 1/3" x 4" inches and 6 per page. Just need logo and address listed at top of the label and white space at bottom.

Company: Brantley Estates
Address: 5120 Ridgemont Pkwy. Suite 400, Atlanta, GA 30327
Phone: 770.245.6274
Fax: 770.245.6219 (probably not needed)
Website: www.brantleyestates.com

Thank you for all your help!

Target Market(s)

Should communicate a strong corporate feel

Contact Information for Business Card

Include - logo, name - Martin E. Caldwell, Title - Chairman & CEO, 5120 Ridgemont Pkwy. Suite 400, Atlanta, GA 30327 - Cell number 404.617.####, Office 770.245.62## email@brantleyestates.com; www.brantleyestates.com.

Logo Text

Brantley Estates

Colors

Designer to choose colors to be used in the design.

Requirements
Must have
• Our logo MUST be in full color and not as white. It is preferred that the logo is on a white background.
• Colors - Color code Blue R 0. G 62. B 124 ( #003E7C )
• C 100 M84 Y 26 K 22
Nice to have
• Font used in logo TRAJAN PRO3 PRO BOLD. Would love to see options of both a one sided and double-sided.
Should not have
• Logo in white.

```html
<!DOCTYPE html>
<html lang="en">
<head>
<meta charset="utf-8">
<title>Brantley Estates – Business Card</title>
<link href="https://fonts.googleapis.com/css2?family=Cinzel:wght@700&family=Open+Sans:wght@400;600&display=swap" rel="stylesheet">
<style>
  :root {
    --brand-blue: #003e7c;
    --ink: #201e1e;
    --text-grey: #555555;
    --paper: #ffffff;
    --backdrop: #2c2c2c;
  }
  * { margin: 0; padding: 0; box-sizing: border-box; }
  html, body { width: 1200px; height: 892px; overflow: hidden; }
  body {
    background: var(--backdrop);
    position: relative;
    font-family: "Open Sans", Arial, sans-serif;
  }
  .card {
    position: absolute;
    width: 560px;
    height: 320px;
    background: var(--paper);
    box-shadow: 0 10px 28px rgba(0,0,0,0.45);
    overflow: hidden;
  }
  .card--back { left: 70px; top: 90px; }
  .card--front { left: 570px; top: 480px; }

  .brand-mark {
    position: absolute;
    display: flex;
    align-items: center;
    gap: 10px;
  }
  .brand-mark__dot {
    border-radius: 50%;
    background: var(--brand-blue);
    flex: none;
  }
  .brand-mark__name {
    font-family: "Cinzel", "Times New Roman", serif;
    font-weight: 700;
    color: var(--brand-blue);
    line-height: 1;
  }
  .brand-mark__name span { display: block; }

  /* back side */
  .card--back .brand-mark { right: 40px; bottom: 80px; }
  .card--back .brand-mark__dot { width: 46px; height: 46px; }
  .card--back .brand-mark__name { font-size: 17px; }
  .card--back .brand-mark__name .line-2 { font-size: 11px; letter-spacing: 4px; margin-top: 4px; }
  .website {
    position: absolute;
    right: 40px;
    bottom: 44px;
    font-size: 13px;
    color: var(--text-grey);
  }

  /* front side */
  .accent-band {
    position: absolute;
    left: 0;
    top: 166px;
    width: 100px;
    height: 36px;
    background: var(--brand-blue);
  }
  .card--front .brand-mark { left: 76px; top: 140px; gap: 12px; }
  .card--front .brand-mark__dot { width: 60px; height: 60px; }
  .card--front .brand-mark__name { font-size: 30px; }
  .card--front .brand-mark__name .line-2 { font-size: 14px; letter-spacing: 8px; margin-top: 4px; }

  .accent-tab {
    position: absolute;
    right: 0;
    top: 74px;
    width: 30px;
    height: 26px;
    background: var(--brand-blue);
  }
  .contact {
    position: absolute;
    right: 40px;
    top: 68px;
    text-align: right;
  }
  .contact__name {
    font-weight: 600;
    font-size: 19px;
    color: var(--brand-blue);
    letter-spacing: 0.3px;
  }
  .contact__title {
    font-size: 11px;
    color: var(--ink);
    margin-bottom: 14px;
  }
  .contact__line {
    font-size: 12px;
    color: var(--text-grey);
    line-height: 17px;
    display: flex;
    justify-content: flex-end;
    align-items: center;
    gap: 6px;
  }
  .contact__line svg { width: 11px; height: 11px; fill: var(--brand-blue); flex: none; }
  .contact__email {
    position: absolute;
    right: 40px;
    bottom: 60px;
    font-size: 12px;
    color: var(--text-grey);
  }
</style>
</head>
<body>

<section class="card card--back" aria-label="Business card, back">
  <div class="brand-mark">
    <div class="brand-mark__dot"></div>
    <div class="brand-mark__name"><span class="line-1">BRANTLEY</span><span class="line-2">ESTATES</span></div>
  </div>
  <p class="website">www.brantleyestates.com</p>
</section>

<section class="card card--front" aria-label="Business card, front">
  <div class="accent-band"></div>
  <div class="brand-mark">
    <div class="brand-mark__dot"></div>
    <div class="brand-mark__name"><span class="line-1">BRANTLEY</span><span class="line-2">ESTATES</span></div>
  </div>

  <div class="accent-tab"></div>
  <div class="contact">
    <p class="contact__name">MARTIN E. CALDWELL</p>
    <p class="contact__title">CHAIRMAN, CEO</p>
    <p class="contact__line">5120 Ridgemont Pkwy.</p>
    <p class="contact__line">Suite 400, Atlanta, GA 30327</p>
    <p class="contact__line">770.245.6274
      <svg viewBox="0 0 12 12" aria-hidden="true"><path d="M1 4c0-2 2-3 5-3s5 1 5 3l-2 1-1-1H4L3 5 1 4zM2 6h8l1 5H1z"/></svg>
    </p>
    <p class="contact__line">404.617.3852
      <svg viewBox="0 0 12 12" aria-hidden="true"><path d="M3 0h6v12H3zM4 1.5v8h4v-8z"/></svg>
    </p>
  </div>
  <p class="contact__email">email@brantleyestates.com</p>
</section>

</body>
</html>
```